The Brushwick Art Gallery

I need to have logo art from my business sign (see attached. Note: NO NEW DESIGN NEEDED, just vector art from my sign) for my Business Card, Letterhead, Envelope and in the future use in a website. I do need a layout for my business card, letterhead and envelopes.

PLEASE USE THE SAME ARTWORK FROM MY SIGN!!!!!

Target Market(s)

Contemporary Art Buyers, 25-50 years of age

Industry/Entity Type

Business

Logo Text

The Brushwick (below..Art Gallery & Studio)

Requirements
Must have
• The same design as my sign

```html
<!DOCTYPE html>
<html lang="en">
<head>
<meta charset="utf-8">
<title>The Brushwick – Stationery</title>
<link href="https://fonts.googleapis.com/css2?family=Lato:ital,wght@0,400;0,700;1,400&display=swap" rel="stylesheet">
<style>
  :root {
    --backdrop: #464646;
    --paper: #ffffff;
    --brand-brown: #6b5427;
    --rule-gold: #8a6a2e;
    --shadow: rgba(0,0,0,.65);
  }
  * { margin: 0; padding: 0; box-sizing: border-box; }
  html, body { width: 1200px; height: 1000px; overflow: hidden; }
  body {
    background: var(--backdrop);
    font-family: "Lato", Arial, sans-serif;
    color: var(--brand-brown);
    position: relative;
  }
  .sheet {
    position: absolute;
    background: var(--paper);
    box-shadow: 7px 7px 7px var(--shadow);
    overflow: hidden;
  }
  .brand-mark {
    position: absolute;
    display: flex;
    align-items: center;
    gap: 5px;
    font-weight: 700;
    color: var(--brand-brown);
    white-space: nowrap;
  }
  .brand-mark .dot {
    border-radius: 50%;
    background: var(--brand-brown);
    flex: none;
  }
  .gold-rule {
    position: absolute;
    height: 4px;
    background: radial-gradient(ellipse at center, var(--rule-gold) 0%, var(--rule-gold) 40%, rgba(138,106,46,0) 100%);
    border-radius: 50%;
  }
  .contact {
    position: absolute;
    text-align: center;
    font-weight: 700;
    line-height: 11px;
    white-space: nowrap;
  }
  .phone-icon { width: 9px; height: 9px; vertical-align: -1px; }

  /* Letterhead */
  .letterhead { width: 512px; height: 725px; }
  .letterhead.back { left: 64px; top: 140px; }
  .letterhead.front { left: 39px; top: 120px; }
  .letterhead .brand-mark { left: 0; right: 0; top: 56px; justify-content: center; font-size: 15px; }
  .letterhead .brand-mark .dot { width: 10px; height: 10px; }
  .letterhead .gold-rule { left: 66px; width: 376px; top: 663px; }
  .letterhead .contact { left: 0; right: 0; top: 676px; font-size: 8.5px; }

  /* Envelope */
  .envelope { width: 507px; height: 253px; }
  .envelope.back { left: 665px; top: 269px; }
  .envelope.front { left: 641px; top: 249px; }
  .envelope .brand-mark { left: 40px; top: 36px; font-size: 13px; }
  .envelope .brand-mark .dot { width: 9px; height: 9px; }
  .envelope .contact { left: 20px; width: 130px; top: 74px; font-size: 8px; line-height: 10px; }

  /* Business card */
  .card { width: 259px; height: 148px; }
  .card.back { left: 790px; top: 588px; }
  .card.front { left: 765px; top: 568px; }
  .card .brand-mark { left: 17px; top: 24px; font-size: 10px; gap: 4px; }
  .card .brand-mark .dot { width: 7px; height: 7px; }
  .card .holder { position: absolute; left: 0; right: 0; top: 62px; text-align: center; }
  .card .holder-name { font-size: 16px; font-weight: 700; line-height: 18px; }
  .card .holder-role { font-size: 12px; font-style: italic; line-height: 13px; }
  .card .gold-rule { left: 12px; width: 235px; top: 119px; height: 2px; }
  .card .contact { left: 0; right: 0; top: 123px; font-size: 8px; line-height: 11px; }
</style>
</head>
<body>

<svg width="0" height="0" style="position:absolute">
  <defs>
    <symbol id="phone" viewBox="0 0 20 20">
      <circle cx="10" cy="10" r="8.6" fill="none" stroke="currentColor" stroke-width="1.8"/>
      <path d="M7 5.6c.6-.3 1 0 1.3.6l.7 1.5c.2.5 0 .9-.4 1.2l-.5.4c.5 1.2 1.3 2 2.5 2.6l.4-.5c.3-.4.8-.5 1.2-.3l1.5.7c.6.3.8.8.5 1.3-.5 1-1.5 1.5-2.6 1.1C9.2 13.4 6.8 11 6 8.6c-.4-1.2 0-2.4 1-3z" fill="currentColor"/>
    </symbol>
  </defs>
</svg>

<!-- Letterhead -->
<section class="sheet letterhead back">
  <div class="contact">
    The Brushwick<br>
    42 W Harbor Street , P.O. Box 3170 , Millbrook, MI 49512 USA<br>
    <svg class="phone-icon"><use href="#phone"/></svg> : 555-014-2786
  </div>
</section>
<section class="sheet letterhead front">
  <div class="brand-mark"><span class="dot"></span>The Brushwick</div>
  <div class="gold-rule"></div>
  <div class="contact">
    The Brushwick<br>
    42 W Harbor Street , P.O. Box 3170 , Millbrook, MI 49512 USA<br>
    <svg class="phone-icon"><use href="#phone"/></svg> : 555-014-2786
  </div>
</section>

<!-- Envelope -->
<section class="sheet envelope back"></section>
<section class="sheet envelope front">
  <div class="brand-mark"><span class="dot"></span>The Brushwick</div>
  <div class="contact">
    42 W Harbor Street . P.O. Box 3170<br>
    Millbrook, MI 49512 USA
  </div>
</section>

<!-- Business card -->
<section class="sheet card back">
  <div class="gold-rule"></div>
  <div class="contact">
    42 W Harbor Street, P.O. Box 3170 , Millbrook, MI 49512 USA<br>
    <svg class="phone-icon"><use href="#phone"/></svg> : 555-014-2786
  </div>
</section>
<section class="sheet card front">
  <div class="brand-mark"><span class="dot"></span>The Brushwick</div>
  <div class="holder">
    <div class="holder-name">Daniel J. Hartley</div>
    <div class="holder-role">Owner/Artist</div>
  </div>
  <div class="gold-rule"></div>
  <div class="contact">
    42 W Harbor Street, P.O. Box 3170 , Millbrook, MI 49512 USA<br>
    <svg class="phone-icon"><use href="#phone"/></svg> : 555-014-2786
  </div>
</section>

</body>
</html>
```